WP website design (Brenmoor)

We need a wordpress design for an established auction and real estate company based in Kentucky. The winning design will incorporate a professional color scheme with company logo in a clean layout with specified widgets. The design needs to consider that this will be developed on a responsive theme. Color is #307d84, with gray/black or other as an accent/highlight color.

Industry/Entity Type

Real Estate

Requirements
Must have
• Elelments of design need to consider that this site is going to be developed on a responsive theme.

Navigation:
1) Home 2) Current Auctions 3) Past Auctions 4) Meet the Staff 5) For Sellers 6) For Buyers 7) Testimonials 8) Contact Us

Colors will be the blue of logo plus black/gray or other accent color.

Slideshow will be prominent, please use stock real estate photo for initial image. Will have following in either header or sidebar: testimonials, social icons (FB, linkedin Twitter, RSS), Featured Auctions widget, newsletter signup form.

Footer will have contact info (below) and attached affiliation logos.
Brenmoor Auctions, Inc.
8415 Tamsen Rd., Louisville KY 40291
glen.office@brenmoorbid.example
Phone: (502) 736 2048

```html
<!DOCTYPE html>
<html lang="en">
<head>
<meta charset="utf-8">
<title>Brenmoor Auctions inc.</title>
<link href="https://fonts.googleapis.com/css2?family=Source+Sans+3:wght@400;600;700&family=Arimo:ital,wght@0,400;0,700;1,400&display=swap" rel="stylesheet">
<style>
:root{
  --teal:#307d84;
  --teal-dark:#276a70;
  --gold:#f2c46d;
  --gold-dark:#d9a445;
  --ink:#222;
  --heading:#555;
  --page:#f2f2f2;
  --header:#f7f7f7;
  --line:#c9c9c9;
  --footer:#222;
  --footer-bottom:#171717;
}
*{box-sizing:border-box;margin:0;padding:0}
html,body{width:899px;height:1200px;overflow:hidden}
body{position:relative;background:var(--page);font-family:"Arimo",Arial,sans-serif;color:var(--ink)}
.abs{position:absolute}

.main-nav{left:0;top:0;width:899px;height:32px;background:var(--teal);display:flex;align-items:center;padding-left:82px}
.main-nav a{font-family:"Source Sans 3",sans-serif;font-weight:600;font-size:9.6px;color:#fff;text-decoration:none;padding:4px 5px;border-radius:3px;margin-right:12px;position:relative}
.main-nav a+a::before{content:"";position:absolute;left:-9px;top:2px;height:14px;border-left:1px solid rgba(255,255,255,.35)}
.main-nav a.is-active{background:var(--gold);color:#333}

.site-header{left:0;top:32px;width:899px;height:100px;background:var(--header)}
.brand{left:77px;top:26px;display:flex;align-items:center;gap:8px}
.brand-mark{width:14px;height:14px;background:var(--teal)}
.brand-name{font-family:"Source Sans 3",sans-serif;font-weight:700;font-size:25px;color:var(--teal);line-height:1}
.social{left:527px;top:44px;display:flex;align-items:center;gap:8px}
.social-label{font-family:"Source Sans 3",sans-serif;font-size:21px;color:#555;margin-right:8px;letter-spacing:.5px}
.social-link{width:30px;height:28px;background:var(--teal);color:#fff;font-size:7px;display:flex;align-items:center;justify-content:center;border-radius:3px;text-decoration:none}

.hero{left:0;top:132px;width:899px;height:334px;background:linear-gradient(180deg,#4d6f97 0%,#93a9c3 45%,#9c9380 68%,#4a5a35 85%,#2f3a22 100%)}

.welcome-title{left:86px;top:489px;font-family:"Source Sans 3",sans-serif;font-weight:600;font-size:21px;color:var(--heading)}
.welcome-text{left:87px;top:520px;width:474px;font-size:10.4px;line-height:15.2px}
.section-title{left:86px;top:611px;font-family:"Source Sans 3",sans-serif;font-weight:600;font-size:21px;color:var(--heading)}

.auction-card{left:86px;width:465px;height:199px;background:#fff;border:1px solid var(--line);border-radius:3px}
.auction-card h3{position:absolute;left:10px;top:13px;font-size:10.4px;letter-spacing:.6px;color:var(--teal);font-weight:700}
.auction-photo{position:absolute;left:10px;top:38px;width:113px;height:71px;background:linear-gradient(180deg,#a8b9a6 0%,#3f8a6b 30%,#c6c1b0 55%,#6a5d56 80%,#3c3834 100%)}
.auction-meta{position:absolute;left:137px;top:37px;font-size:10px;line-height:12.5px}
.auction-meta .kind{font-weight:700;font-size:9px;margin-bottom:4px}
.auction-meta p+p{margin-top:9px}
.details-btn{position:absolute;left:10px;top:125px;width:113px;height:28px;border:1px solid #a8812f;border-radius:3px;background:linear-gradient(180deg,#f6d58c,var(--gold-dark));display:flex;align-items:center;justify-content:center;gap:8px;font-size:13.5px;color:#222}
.auction-desc{position:absolute;left:135px;top:122px;width:323px;font-size:10.2px;line-height:13.6px}
.bid-link{position:absolute;left:135px;top:170px;font-size:10.2px;color:var(--teal)}

.newsletter{left:578px;top:487px;width:238px;height:128px;background:var(--teal);border-radius:3px;color:#fff;padding:12px 16px}
.newsletter h2{font-family:"Source Sans 3",sans-serif;font-weight:700;font-size:21px}
.newsletter p{font-size:10px;line-height:13.5px;margin-top:5px}
.signup{display:flex;margin-top:11px;width:200px;height:23px}
.signup span{flex:1;background:#fff;font-size:10px;color:#999;padding:5px 8px}
.signup b{width:35px;background:var(--gold);color:#222;font-size:10.5px;display:flex;align-items:center;justify-content:center}

.widget{left:578px;width:238px;background:#fff;border:1px solid var(--line);border-radius:3px;padding:10px 17px}
.widget h2{font-family:"Source Sans 3",sans-serif;font-weight:600;font-size:21px;color:var(--teal)}
.featured{top:634px;height:212px}
.featured h4{font-size:10px;margin:6px 2px 3px}
.featured-photo{width:198px;height:73px;background:linear-gradient(180deg,#a8b9a6 0%,#3f8a6b 30%,#c6c1b0 55%,#6a5d56 80%,#3c3834 100%)}
.featured p{font-size:9.6px;line-height:12px;margin-top:9px}
.testimonials{top:868px;height:200px}
.testimonials blockquote{font-style:italic;font-size:10.2px;line-height:14.9px;margin-top:8px;color:#333}
.testimonials cite{display:block;text-align:right;font-size:10px;color:var(--gold-dark);text-decoration:underline;margin-top:6px;font-weight:700}

.site-footer{left:0;top:1090px;width:899px;height:82px;background:var(--footer);color:#eee}
.contact{position:absolute;left:81px;top:12px;font-size:10.5px;line-height:15.2px}
.badges{position:absolute;left:511px;top:14px;display:flex;gap:18px;align-items:center}
.badge{background:#888;height:46px}
.copyright{left:0;top:1172px;width:899px;height:28px;background:var(--footer-bottom);color:#ccc;font-size:10.4px;text-align:center;line-height:28px}
</style>
</head>
<body>

<nav class="main-nav abs">
  <a>HOME</a><a class="is-active">CURRENT AUCTIONS</a><a>PAST AUCTIONS</a><a>MEET THE STAFF</a><a>FOR SELLERS</a><a>FOR BUYERS</a><a>TESTIMONIALS</a><a>CONTACT US</a>
</nav>

<header class="site-header abs">
  <div class="brand abs"><span class="brand-mark"></span><span class="brand-name">Brenmoor Auctions inc.</span></div>
  <div class="social abs">
    <span class="social-label">Social Media:</span>
    <a class="social-link">FB</a><a class="social-link">LI</a><a class="social-link">TW</a><a class="social-link">RSS</a>
  </div>
</header>

<div class="hero abs" role="img" aria-label="Lit white colonial estate home with palm trees at dusk"></div>

<h1 class="welcome-title abs">Welcome to Brenmoor Auction inc.</h1>
<p class="welcome-text abs">Brenmoor Auctions Inc. is a full time auction company engaged in the marketing and sale of real estate and personal property by auction.The auctioneers with Brenmoor Auctions are licensed to do business in the States of Kentucky, and Indiana. Their clients include numerous individuals, attorneys, banks, municipal agencies and the U.S. Bankruptcy Court.&nbsp; The four principle auctioneers in the company have a combined 90 years of experience in the auction business.</p>

<h2 class="section-title abs">Current Auction</h2>

<article class="auction-card abs" style="top:646px">
  <h3>ABSOLUTE ONLINE ONLY AUCTION – PERSONAL PROPERTY</h3>
  <div class="auction-photo" role="img" aria-label="Crowd gathered in front of a house at an on-site auction"></div>
  <div class="auction-meta">
    <div class="kind">LIVE ON-SITE AUCTION</div>
    <p><b>Begins:</b>&nbsp; Saturday, March 16, 2013<br>at 10:00 AM EDT</p>
    <p><b>Location:</b>&nbsp; 5128 Halvers Road<br>Bagdad, KY 40003</p>
  </div>
  <div class="details-btn"><svg width="16" height="16" viewBox="0 0 16 16"><circle cx="6.5" cy="6.5" r="4.5" fill="none" stroke="#222" stroke-width="2.2"/><line x1="10" y1="10" x2="14.5" y2="14.5" stroke="#222" stroke-width="2.6" stroke-linecap="round"/></svg>Details</div>
  <p class="auction-desc">Kessler BS3F High Lift, 600 Series Harlan tractor w/Norvale Loader, Dune buggy, 1207 HT Cutditioner: SHOP &amp; MISCELLANIOUS &amp; PORK PROCESSING ITEMS. Electric welders, acetylene tanks and torches.</p>
  <a class="bid-link">Click here for our online bidding site.</a>
</article>

<article class="auction-card abs" style="top:868px">
  <h3>ABSOLUTE ONLINE ONLY AUCTION – PERSONAL PROPERTY</h3>
  <div class="auction-photo" role="img" aria-label="Crowd gathered in front of a house at an on-site auction"></div>
  <div class="auction-meta">
    <div class="kind">LIVE ON-SITE AUCTION</div>
    <p><b>Begins:</b>&nbsp; Saturday, March 16, 2013<br>at 10:00 AM EDT</p>
    <p><b>Location:</b>&nbsp; 5128 Halvers Road<br>Bagdad, KY 40003</p>
  </div>
  <div class="details-btn"><svg width="16" height="16" viewBox="0 0 16 16"><circle cx="6.5" cy="6.5" r="4.5" fill="none" stroke="#222" stroke-width="2.2"/><line x1="10" y1="10" x2="14.5" y2="14.5" stroke="#222" stroke-width="2.6" stroke-linecap="round"/></svg>Details</div>
  <p class="auction-desc">Kessler BS3F High Lift, 600 Series Harlan tractor w/Norvale Loader, Dune buggy, 1207 HT Cutditioner: SHOP &amp; MISCELLANIOUS &amp; PORK PROCESSING ITEMS. Electric welders, acetylene tanks and torches.</p>
  <a class="bid-link">Click here for our online bidding site.</a>
</article>

<aside class="newsletter abs">
  <h2>Newsletter Sign up</h2>
  <p>Sign up for our free messages &amp; receive auction alerts.</p>
  <div class="signup"><span>Email Address</span><b>GO</b></div>
</aside>

<aside class="widget featured abs">
  <h2>Featured Auction</h2>
  <h4>Multi Estate &amp; Consignment Auction</h4>
  <div class="featured-photo" role="img" aria-label="Auction crowd outside a house with a green roof"></div>
  <p><b>Start Date/ Time:</b> Saturday, April 13,<br>2013 At 10:00 Am</p>
  <p><b>Location:</b> 1904 Old Carrow,&nbsp; 73812</p>
</aside>

<aside class="widget testimonials abs">
  <h2>Testimonials</h2>
  <blockquote>“ Lorem Ipsum has been the industry's standard dummy text ever since the 1500s, when an unknown printer took a galley of type and scrambled it to make a type speci men book.It has survived not only five centuries, but also the leap into electronic typesetting, remaining essentially unchanged. ”</blockquote>
  <cite>Dalen Moore</cite>
</aside>

<footer class="site-footer abs">
  <address class="contact" style="font-style:normal">Brenmoor Auctions, Inc.<br>8415 Tamsen Rd., Louisville KY 40291<br>glen.office@brenmoorbid.example<br>Phone: (502) 736 2048</address>
  <div class="badges" aria-label="Affiliation badges">
    <span class="badge" style="width:90px;height:40px;border-radius:50%"></span>
    <span class="badge" style="width:36px"></span>
    <span class="badge" style="width:30px"></span>
    <span class="badge" style="width:42px"></span>
    <span class="badge" style="width:34px"></span>
  </div>
</footer>
<div class="copyright abs">Copyright © 2014 Brenmoor Auction inc All Rights Reserved.</div>

</body>
</html>
```